New professional looking flyer for company

I need our flyer updated my flyer is the Ruv flyer Have attached current flyer so you know what services need to be listed. Want it to be in mainly dark colours like black and dark grey with pops of light grey, silver or white. i have added several photos for you to choose which ones work best with your design would like The photos to be in colour for the flyer. But can have a mix of greyscale if that works for your design j have attached another companies flyers as design ideas to show what I am looking for

Target Market(s)

new clients

Industry/Entity Type

transport and earthmoving

Colors

Designer to choose colors to be used in the design.

Requirements
Nice to have
• Look professional
Should not have
• No orange or red or green

```html
<!DOCTYPE html>
<html lang="en">
<head>
<meta charset="utf-8">
<title>Ruv Pty Ltd – Our Services</title>
<link rel="stylesheet" href="https://fonts.googleapis.com/css2?family=Lato:wght@300;700&family=Montserrat:wght@800&family=Poppins:wght@400&display=swap">
<style>
  :root {
    --page-bg: #e9e6e7;
    --ink-black: #000000;
    --flyer-dark: #05070a;
    --panel-grey: #1c1d20;
    --panel-grey-deep: #0b0c0e;
    --silver-light: #e8e8ea;
    --silver-mid: #9a9ca0;
    --silver-dark: #55575b;
    --text-white: #ffffff;
    --text-dark: #111111;
    --paper-white: #ffffff;
  }
  * { box-sizing: border-box; margin: 0; padding: 0; }
  html, body { width: 1200px; height: 2400px; overflow: hidden; }
  body { background: var(--page-bg); position: relative; }

  .flyer {
    position: absolute; left: 48px; top: 440px;
    width: 1104px; height: 1429px;
    background: var(--flyer-dark);
    overflow: hidden;
  }
  .top-band { position: absolute; left: 0; top: 0; width: 100%; height: 98px; background: var(--ink-black); }

  .site-backdrop {
    position: absolute; left: 0; top: 460px; width: 100%; height: 700px;
    background: radial-gradient(ellipse at 75% 55%, #2a2620 0%, #141312 40%, var(--flyer-dark) 75%);
    opacity: .8;
  }

  .brand-shield { position: absolute; left: 335px; top: 0; width: 455px; height: 412px; }
  .brand-name {
    position: absolute; left: 335px; top: 200px; width: 455px;
    text-align: center; font-family: "Lato", sans-serif; font-weight: 700;
    font-size: 58px; letter-spacing: 2px; color: var(--silver-light);
  }

  .truck-photo { position: absolute; border-radius: 6px; }
  .truck-left {
    left: 0; top: 136px; width: 408px; height: 291px;
    background: linear-gradient(160deg, #2c3340 0%, #1a1d24 45%, #8a7c5a 80%, #3a3328 100%);
  }
  .truck-right {
    left: 683px; top: 184px; width: 421px; height: 320px;
    background: linear-gradient(200deg, #b7b9bd 0%, #d9dadc 35%, #7d7f84 65%, #8b7a3c 100%);
  }

  .services-title {
    position: absolute; left: 60px; top: 508px;
    font-family: "Montserrat", sans-serif; font-weight: 800; font-size: 52px;
    letter-spacing: 1px;
    background: linear-gradient(180deg, #ffffff 0%, #c9cacd 50%, #6f7175 100%);
    -webkit-background-clip: text; background-clip: text; color: transparent;
  }

  .service { position: absolute; width: 340px; height: 66px; }
  .service-icon {
    position: absolute; left: 0; top: 0; width: 65px; height: 65px;
    border: 2px solid var(--text-white); border-radius: 50%;
    display: flex; align-items: center; justify-content: center;
  }
  .service-icon svg { width: 34px; height: 34px; fill: none; stroke: var(--text-white); stroke-width: 1.6; stroke-linecap: round; stroke-linejoin: round; }
  .service-label {
    position: absolute; top: 50%; transform: translateY(-50%);
    font-family: "Lato", sans-serif; font-weight: 300; font-size: 17px;
    line-height: 20px; color: var(--text-white);
  }

  .paper-footer { position: absolute; left: 0; top: 1080px; width: 100%; height: 349px; }
  .closing-line {
    position: absolute; left: 0; top: 1210px; width: 100%;
    text-align: center; font-family: "Poppins", sans-serif; font-size: 28px;
    line-height: 33px; color: var(--text-dark);
  }
  .contact { position: absolute; top: 1316px; height: 54px; display: flex; align-items: center; }
  .contact-icon {
    width: 53px; height: 53px; border-radius: 50%; background: var(--ink-black);
    display: flex; align-items: center; justify-content: center; flex: none;
  }
  .contact-icon svg { width: 26px; height: 26px; fill: none; stroke: var(--text-white); stroke-width: 1.6; stroke-linecap: round; stroke-linejoin: round; }
  .contact-text {
    margin-left: 24px; font-family: "Lato", sans-serif; font-weight: 700;
    font-size: 13px; color: var(--text-dark);
  }
</style>
</head>
<body>
<main class="flyer">
  <div class="top-band"></div>
  <div class="site-backdrop" role="img" aria-label="Faint photo of a loader working on an earthworks site"></div>

  <div class="truck-photo truck-left" role="img" aria-label="Photo of a dark prime mover truck with bull bar"></div>
  <div class="truck-photo truck-right" role="img" aria-label="Photo of a white prime mover hauling an oversize load"></div>

  <svg class="brand-shield" viewBox="0 0 455 412" aria-hidden="true">
    <defs>
      <linearGradient id="shieldEdge" x1="0" y1="0" x2="1" y2="1">
        <stop offset="0" stop-color="#f2f2f3"/>
        <stop offset=".5" stop-color="#8d8f93"/>
        <stop offset="1" stop-color="#e0e1e3"/>
      </linearGradient>
      <radialGradient id="shieldFill" cx=".5" cy=".4" r=".7">
        <stop offset="0" stop-color="#2a2b2e"/>
        <stop offset="1" stop-color="#0b0c0e"/>
      </radialGradient>
    </defs>
    <path d="M0 0 H455 V322 L227.5 412 L0 322 Z" fill="url(#shieldEdge)"/>
    <path d="M14 6 H441 V312 L227.5 396 L14 312 Z" fill="url(#shieldFill)"/>
  </svg>
  <div class="brand-name">Ruv Pty Ltd</div>

  <h1 class="services-title">OUR SERVICES</h1>

  <!-- column one -->
  <div class="service" style="left:93px;top:617px">
    <div class="service-icon"><svg viewBox="0 0 34 34"><path d="M6 4 L12 26 H28"/><rect x="13" y="10" width="11" height="9"/><circle cx="14" cy="29" r="2.5"/></svg></div>
    <div class="service-label" style="left:70px">Over size loads<br>/ Hot Shot Loads</div>
  </div>
  <div class="service" style="left:93px;top:712px">
    <div class="service-icon"><svg viewBox="0 0 34 34"><path d="M9 24 A7 7 0 0 1 10 11 A9 9 0 0 1 26 13 A6 6 0 0 1 25 24 Z"/><path d="M13 19 A4 4 0 1 0 17 15"/><path d="M17 12 V16 H13"/></svg></div>
    <div class="service-label" style="left:70px">Heavy Vehicle<br>Recovery Services</div>
  </div>
  <div class="service" style="left:93px;top:810px">
    <div class="service-icon"><svg viewBox="0 0 34 34"><path d="M17 4 C12 13 9 18 9 22 A8 8 0 0 0 25 22 C25 18 22 13 17 4 Z"/></svg></div>
    <div class="service-label" style="left:70px">Potable Water Deliveries</div>
  </div>
  <div class="service" style="left:93px;top:922px">
    <div class="service-icon"><svg viewBox="0 0 34 34"><circle cx="17" cy="9" r="5"/><path d="M17 14 V18 M8 18 H26 M8 18 V22 M17 18 V22 M26 18 V22"/><circle cx="8" cy="26" r="3.5"/><circle cx="17" cy="26" r="3.5"/><circle cx="26" cy="26" r="3.5"/></svg></div>
    <div class="service-label" style="left:72px">Mine Site accredited<br>equipment &amp; Operators</div>
  </div>

  <!-- column two -->
  <div class="service" style="left:502px;top:617px">
    <div class="service-icon"><svg viewBox="0 0 34 34"><circle cx="10" cy="8" r="3"/><path d="M22 10 A3 3 0 0 1 28 10 H22"/><rect x="8" y="16" width="20" height="3"/><path d="M11 19 V28 M17 19 V28 M23 19 V28 M4 22 V28"/></svg></div>
    <div class="service-label" style="left:71px">Earthworks</div>
  </div>
  <div class="service" style="left:502px;top:712px">
    <div class="service-icon"><svg viewBox="0 0 34 34"><path d="M7 27 L20 14 A5 5 0 0 0 26 7 L22 11 L20 9 L24 5 A5 5 0 0 0 17 11 L5 24"/><path d="M8 7 L27 26 M7 10 L10 7"/></svg></div>
    <div class="service-label" style="left:71px">Sand &amp; Metal<br>Supply &amp; Cartage</div>
  </div>
  <div class="service" style="left:502px;top:810px">
    <div class="service-icon"><svg viewBox="0 0 34 34"><rect x="9" y="6" width="16" height="20" rx="3"/><rect x="12" y="10" width="10" height="6"/><circle cx="13" cy="21" r="1.2"/><circle cx="21" cy="21" r="1.2"/><path d="M11 26 L8 30 M23 26 L26 30 M14 3 H20"/></svg></div>
    <div class="service-label" style="left:72px">Road Train<br>Tippers</div>
  </div>
  <div class="service" style="left:502px;top:922px">
    <div class="service-icon"><svg viewBox="0 0 34 34"><path d="M8 8 H26 M17 8 V24 M6 24 H28"/><circle cx="11" cy="27" r="2"/><circle cx="23" cy="27" r="2"/></svg></div>
    <div class="service-label" style="left:72px">Road Train<br>Tankers</div>
  </div>

  <!-- column three -->
  <div class="service" style="left:864px;top:617px">
    <div class="service-icon"><svg viewBox="0 0 34 34"><path d="M4 16 L11 7 H14 A3 3 0 0 0 20 7 H23 L30 16 L26 19 L24 16 V27 H10 V16 L8 19 Z"/></svg></div>
    <div class="service-label" style="left:92px">Road Train<br>Flat Tops</div>
  </div>
  <div class="service" style="left:864px;top:712px">
    <div class="service-icon"><svg viewBox="0 0 34 34"><rect x="10" y="10" width="20" height="10" rx="1"/><rect x="13" y="13" width="4" height="3"/><rect x="19" y="13" width="4" height="3"/><rect x="25" y="13" width="3" height="3"/><path d="M4 20 H30 M4 16 V24"/><circle cx="15" cy="23" r="2"/><circle cx="24" cy="23" r="2"/></svg></div>
    <div class="service-label" style="left:93px">Drop Deck<br>Trailers</div>
  </div>
  <div class="service" style="left:864px;top:810px">
    <div class="service-icon"><svg viewBox="0 0 34 34"><path d="M14 5 H20 L26 27 H8 Z"/><path d="M12 13 H22 M10 20 H24 M5 27 H29"/></svg></div>
    <div class="service-label" style="left:93px">Road Building<br>/ Maintenance</div>
  </div>

  <svg class="paper-footer" viewBox="0 0 1104 349" preserveAspectRatio="none" aria-hidden="true">
    <defs>
      <linearGradient id="paperFade" x1="0" y1="0" x2="0" y2="1">
        <stop offset="0" stop-color="#ffffff" stop-opacity="0"/>
        <stop offset=".2" stop-color="#ffffff" stop-opacity=".85"/>
        <stop offset=".34" stop-color="#ffffff"/>
      </linearGradient>
    </defs>
    <path d="M0 80 C180 30 320 70 520 40 C720 15 900 50 1104 20 V349 H0 Z" fill="url(#paperFade)"/>
    <path d="M0 120 C200 90 380 110 560 95 C760 80 920 100 1104 85 V349 H0 Z" fill="#ffffff"/>
  </svg>

  <p class="closing-line">We offer a large range of services not listed so Call us today for<br>personalised quote to suit your needs.</p>

  <div class="contact" style="left:86px">
    <span class="contact-icon"><svg viewBox="0 0 26 26"><path d="M6 3 L10 3 L12 9 L9 11 C10 14 12 16 15 17 L17 14 L23 16 L23 20 C23 22 21 23 19 23 C10 22 4 16 3 7 C3 5 4 3 6 3 Z"/></svg></span>
    <span class="contact-text">555-014-2290</span>
  </div>
  <div class="contact" style="left:424px">
    <span class="contact-icon"><svg viewBox="0 0 26 26"><circle cx="13" cy="13" r="10"/><ellipse cx="13" cy="13" rx="4.5" ry="10"/><path d="M3 13 H23 M5 8 H21 M5 18 H21"/></svg></span>
    <span class="contact-text">www.ruvtransport.com.au</span>
  </div>
  <div class="contact" style="left:803px">
    <span class="contact-icon"><svg viewBox="0 0 26 26"><rect x="3" y="6" width="20" height="14"/><path d="M3 6 L13 14 L23 6 M3 20 L10 12 M23 20 L16 12"/></svg></span>
    <span class="contact-text">sales@ruvtransport.com.au</span>
  </div>
</main>
</body>
</html>
```